Cool cafe needs help with our corporate identity.

We have a logo! We have a font!

What we need is to tie it together for
1. A menu
2. Labels for jam and other things we sell
3. Business Cards

All should have the same design style.

We have a strong design aesthetic in the cafe. Lots of colour and quirky objects. See this Snapvale profile for photos (you can download high-res from here if you sign into Snapvale): http://www.snapvale-example.net/photos/51827094@K03/

Also our website is www.peterwalrus.net

A main feature is the counter that is made of yardsticks.

There is also a bit of and 80's feel. Especially images of Edmund and Bea (the Royals).

We also like weird taxidermy and anthropology images from the 1920s. Harold P. Quimsby was an anthropologist who used to own a Walrus called Peter. That is where our name comes from. Seekly 'Harold P. Quimsby' for interesting images.

Perhaps design elements could be taken from any of these themes, although we are open to other ideas.

We like being playful and irreverent.

The logo is the words Peter Walrus in Cursive. We want to stick with that. The font we like is Tallow Works Voss. The logo is currently blue colour - this can change.

1.Menu Specs
We like printing this ourselves. Thick paper A4 with a fold seems to work well. We want some design elements added. Our existing menu is attached.

2. Labels
We have jam jars and labels for biscuits. These are various sizes. It needs to have the name of the jam,e.g. Apricot, The Peter Walrus Logo, Some design elements, A list of ingredients, and the weight. Eg 250g.

3. Business Card
A standard sized business card with The logo, design elements and the following words:
Peter Walrus Cafe
17 Lindqvist Road, Kellbrook Vale
03 9017 4426
www.peterwalrus.net

Target Market(s)

Adults based in Melbourne, Australia that like design and are kind of hipsterish,

Industry/Entity Type

Printing

Requirements
Must have
• Logo and font as described.
Nice to have
• Maybe a bit quirky.
Should not have
• Slick corporate look.

```html
<!DOCTYPE html>
<html lang="en">
<head>
<meta charset="utf-8">
<title>Peter Walrus Cafe Menu</title>
<link rel="stylesheet" href="https://fonts.googleapis.com/css2?family=Courier+Prime:wght@400;700&family=Libre+Baskerville:ital@0;1&display=swap">
<style>
  :root {
    --backdrop: #d9d9d9;
    --paper: #ffffff;
    --chevron-blue: #8fb4c7;
    --chevron-pale: #c9dde7;
    --coral: #e98873;
    --ink: #2f2f2f;
    --rule: #3a3a3a;
    --muted: #6b6b6b;
  }
  * { box-sizing: border-box; margin: 0; padding: 0; }
  html, body {
    width: 1200px; height: 799px; overflow: hidden;
    background: var(--backdrop);
  }
  body { position: relative; font-family: "Courier Prime", "Courier New", monospace; color: var(--ink); }

  .menu-sheet {
    position: absolute; top: 67px;
    width: 470px; height: 665px;
    background: var(--paper);
    box-shadow: 0 2px 6px rgba(0,0,0,.18);
    overflow: hidden;
  }
  .menu-front { left: 70px; }
  .menu-back { left: 660px; }

  .chevron-field {
    position: absolute;
    background: linear-gradient(160deg, var(--chevron-pale) 0%, var(--chevron-blue) 55%, var(--chevron-pale) 100%);
  }
  .menu-front .chevron-field { left: 0; top: 0; width: 100%; height: 478px; }
  .menu-back .chevron-field { inset: 0; }

  .brand-disc {
    position: absolute; left: 105px; top: 60px;
    width: 260px; height: 260px; border-radius: 50%;
    background: var(--coral);
    display: flex; flex-direction: column; align-items: center; justify-content: center;
    color: var(--paper); text-align: center;
  }
  .brand-name { font-size: 30px; font-weight: 400; line-height: 1; letter-spacing: .5px; }
  .brand-sub { font-size: 13px; letter-spacing: 4px; margin-top: 6px; }
  .brand-contact { font-size: 8.5px; line-height: 1.5; margin-top: 22px; }

  .front-rule { position: absolute; left: 0; top: 478px; width: 100%; height: 5px; background: var(--rule); }
  .ethos {
    position: absolute; left: 0; top: 525px; width: 100%;
    font-family: "Libre Baskerville", Georgia, serif; font-style: italic;
    font-size: 11.5px; line-height: 1.45; text-align: center; color: var(--ink);
  }

  .menu-panel {
    position: absolute; left: 30px; top: 24px; right: 30px; bottom: 26px;
    background: var(--paper);
    padding: 14px 20px 12px;
    display: flex; flex-direction: column;
  }
  .menu-columns { display: grid; grid-template-columns: 1fr 1fr; column-gap: 22px; flex: 1; }
  .menu-section { margin-bottom: 16px; }
  .section-title {
    font-family: "Libre Baskerville", Georgia, serif; font-style: italic;
    font-size: 13px; margin-bottom: 7px;
  }
  .dish { font-size: 8.5px; line-height: 1.35; margin-bottom: 6px; display: flex; justify-content: space-between; gap: 6px; }
  .price { white-space: nowrap; }
  .drink-list .dish { margin-bottom: 2px; padding-right: 40px; }
  .menu-note { font-size: 8px; line-height: 1.4; width: 50%; margin-left: auto; color: var(--muted); }
  .menu-footer { display: flex; justify-content: space-between; font-size: 7.5px; color: var(--muted); margin-top: 10px; }
</style>
</head>
<body>

<section class="menu-sheet menu-front">
  <div class="chevron-field" role="img" aria-label="Pale blue and white zigzag chevron pattern"></div>
  <div class="brand-disc">
    <span class="brand-name">Peter Walrus</span>
    <span class="brand-sub">CAFE</span>
    <p class="brand-contact">17 Lindqvist Road, Kellbrook Vale<br>03 9017 4426<br>www.peterwalrus.net</p>
  </div>
  <div class="front-rule"></div>
  <p class="ethos">Our focus is on quality, local suppliers that have<br>high ethical standards.<br>We use fresh, free range, organic food<br>wherever possible.</p>
</section>

<section class="menu-sheet menu-back">
  <div class="chevron-field" role="img" aria-label="Pale blue and white zigzag chevron border pattern"></div>
  <div class="menu-panel">
    <div class="menu-columns">
      <div class="menu-column">
        <div class="menu-section">
          <h2 class="section-title">Cereals, fruit and toast</h2>
          <p class="dish"><span>House granola, yoghurt and poached pear</span><span class="price">12</span></p>
          <p class="dish"><span>Bircher muesli with apple</span><span class="price">11</span></p>
          <p class="dish"><span>Sourdough toast with jam</span><span class="price">7</span></p>
          <p class="dish"><span>Fruit loaf, butter</span><span class="price">6</span></p>
        </div>
        <div class="menu-section">
          <h2 class="section-title">Breakfast</h2>
          <p class="dish"><span>Walrus breakfast, bacon, beans, eggs</span><span class="price">19</span></p>
          <p class="dish"><span>Corn fritters, relish, rocket</span><span class="price">16</span></p>
          <p class="dish"><span>Mushrooms on toast with feta</span><span class="price">15</span></p>
          <p class="dish"><span>Pancakes, ricotta and berries</span><span class="price">15</span></p>
        </div>
        <div class="menu-section">
          <h2 class="section-title">Eggs</h2>
          <p class="dish"><span>Eggs your way on sourdough</span><span class="price">10</span></p>
          <p class="dish"><span>Add bacon, avocado or spinach</span><span class="price">4</span></p>
          <p class="dish"><span>Baked eggs, chorizo and tomato</span><span class="price">17</span></p>
          <p class="dish"><span>Smashed avocado with poached egg</span><span class="price">15</span></p>
        </div>
      </div>
      <div class="menu-column">
        <div class="menu-section">
          <h2 class="section-title">Sandwiches</h2>
          <p class="dish"><span>Ham, cheese and tomato toastie</span><span class="price">10</span></p>
          <p class="dish"><span>Pulled pork roll, slaw</span><span class="price">13</span></p>
          <p class="dish"><span>Chicken, aioli and rocket</span><span class="price">12</span></p>
        </div>
        <div class="menu-section">
          <h2 class="section-title">Salad</h2>
          <p class="dish"><span>Quinoa, beetroot and goat cheese</span><span class="price">15</span></p>
        </div>
        <div class="menu-section">
          <h2 class="section-title">Kids (under 10)</h2>
          <p class="dish"><span>Toast soldiers with egg</span><span class="price">8</span></p>
          <p class="dish"><span>Mini pancakes</span><span class="price">8</span></p>
        </div>
        <div class="menu-section drink-list">
          <h2 class="section-title">Drinks</h2>
          <p class="dish"><span>Coffee</span><span class="price">4</span></p>
          <p class="dish"><span>Large coffee</span><span class="price">5</span></p>
          <p class="dish"><span>Pot of tea</span><span class="price">5</span></p>
          <p class="dish"><span>Hot chocolate</span><span class="price">5</span></p>
          <p class="dish"><span>Chai latte</span><span class="price">5</span></p>
          <p class="dish"><span>Fresh juice</span><span class="price">7</span></p>
          <p class="dish"><span>Milkshake</span><span class="price">7</span></p>
        </div>
      </div>
    </div>
    <p class="menu-note">Please tell staff about any allergies. Gluten free bread available.</p>
    <div class="menu-footer"><span>@peterwalruscafe</span><span>/peterwalrus</span></div>
  </div>
</section>

</body>
</html>
```